We are an integrated facilities management company.

We aggregate everything related to facilities maintenance. Repair-replacement of equipment and facility space materials from:
Asset gathering and tracking.
Vendor screening, contracting and management.
Service requirement development.
Work order processing and management.
Invoice reconciliation.
Vendor payment.
Reporting.
Capital equipment bids and project management.

Target Market(s)

Retail, hospitality, multi-family housing, long term healthcare.

Industry/Entity Type

Maintenance

Contact Information for Business Card

Professional and bold look. (see logo zip file)

Colors
3377b5
85abd2
cedeed

Requirements
Must have
• N/A
Nice to have
• N/A
Should not have
• N/A

```html
<!DOCTYPE html>
<html lang="en">
<head>
<meta charset="utf-8">
<title>Keystone Facility Partners – Business Card</title>
<link href="https://fonts.googleapis.com/css2?family=Montserrat:wght@400;500;600;700;800&display=swap" rel="stylesheet">
<style>
  :root{
    --brand-blue:#3377b5;
    --brand-blue-deep:#1f5fa3;
    --brand-light:#85abd2;
    --brand-pale:#cedeed;
    --ink:#2b2f36;
    --ink-soft:#5c636d;
    --panel-dark:#15181d;
    --panel-dark-2:#23272e;
    --paper:#ffffff;
    --backdrop:#e9ecf0;
  }
  *{box-sizing:border-box;margin:0;padding:0}
  html,body{width:1200px;height:900px;overflow:hidden}
  body{background:var(--backdrop);font-family:"Montserrat",sans-serif;position:relative}

  .card{position:absolute;left:285px;width:630px;height:360px;overflow:hidden;
        box-shadow:0 10px 30px rgba(20,30,45,.18)}
  .card--front{top:60px;background:var(--paper)}
  .card--back{top:480px;background:var(--brand-blue)}

  /* front */
  .brand{position:absolute;left:250px;top:44px;display:flex;align-items:center;gap:12px}
  .brand__square{width:38px;height:38px;background:var(--brand-blue-deep)}
  .brand__name{font-weight:800;font-size:25px;line-height:1.05;color:var(--brand-blue-deep);text-transform:uppercase;letter-spacing:.5px}
  .brand__tagline{position:absolute;left:300px;top:108px;font-size:9px;letter-spacing:3px;color:var(--ink-soft);text-transform:uppercase}

  .contact{position:absolute;left:40px;top:140px;list-style:none}
  .contact li{display:flex;align-items:center;gap:10px;font-size:13px;font-weight:500;color:var(--ink);height:22px}
  .contact svg{width:14px;height:14px;fill:var(--brand-blue)}

  .front-shapes{position:absolute;inset:0}
  .address{position:absolute;left:40px;top:262px;font-size:13px;font-weight:500;color:var(--ink);letter-spacing:.3px}
  .holder{position:absolute;right:30px;bottom:30px;text-align:right;color:#fff}
  .holder__name{font-weight:700;font-size:17px;letter-spacing:.8px;text-transform:uppercase}
  .holder__role{font-weight:500;font-size:12px;letter-spacing:1.5px;margin-top:3px}

  /* back */
  .services{position:absolute;left:36px;top:34px;width:370px;color:#fff;text-transform:uppercase}
  .services__intro{font-size:10.5px;font-weight:600;line-height:1.45;letter-spacing:.4px;margin-bottom:14px}
  .services__list{list-style:none}
  .services__list li{display:flex;align-items:center;gap:10px;font-size:10.5px;font-weight:600;letter-spacing:.4px;height:24px}
  .services__list li::before{content:"";width:12px;height:12px;border:1.5px solid #fff;flex:none}

  .back-panel{position:absolute;right:0;top:0;width:200px;height:100%;
              background:linear-gradient(160deg,var(--panel-dark-2),var(--panel-dark))}
  .back-brand{position:absolute;left:24px;right:20px;top:130px}
  .back-brand__square{width:30px;height:30px;background:var(--brand-light);margin-bottom:14px}
  .back-brand__name{font-weight:800;font-size:19px;line-height:1.1;color:var(--brand-light);text-transform:uppercase}
  .back-brand__tagline{font-size:7.5px;letter-spacing:2px;color:#9aa3ad;margin-top:10px;text-transform:uppercase}
</style>
</head>
<body>

<section class="card card--front" aria-label="Business card front">
  <svg class="front-shapes" viewBox="0 0 630 360" width="630" height="360" aria-hidden="true">
    <polyline points="0,210 330,288 630,288" fill="none" stroke="var(--brand-blue)" stroke-width="2"/>
    <polygon points="330,288 630,288 630,360 380,360 380,310" fill="var(--brand-blue)"/>
  </svg>

  <div class="brand">
    <span class="brand__square"></span>
    <span class="brand__name">Keystone<br>Facility Partners</span>
  </div>
  <p class="brand__tagline">Maintain · Repair · Replace</p>

  <ul class="contact">
    <li><svg viewBox="0 0 24 24"><path d="M6.6 10.8a15 15 0 0 0 6.6 6.6l2.2-2.2c.3-.3.7-.4 1-.2 1.1.4 2.3.6 3.6.6.6 0 1 .4 1 1V20c0 .6-.4 1-1 1A17 17 0 0 1 3 4c0-.6.4-1 1-1h3.5c.6 0 1 .4 1 1 0 1.3.2 2.5.6 3.6.1.3 0 .7-.2 1z"/></svg>555 014 2620</li>
    <li><svg viewBox="0 0 24 24"><path d="M6 2h12v6H6zM4 9h16a2 2 0 0 1 2 2v6h-4v5H6v-5H2v-6a2 2 0 0 1 2-2zm4 7v4h8v-4z"/></svg>555 014 2620</li>
    <li><svg viewBox="0 0 24 24"><path d="M2 5h20v14H2zm2 2v.5l8 5 8-5V7z"/></svg>marcus@keystonefp.com</li>
    <li><svg viewBox="0 0 24 24"><path d="M12 2a10 10 0 1 0 0 20 10 10 0 0 0 0-20zm6.9 6h-3a15 15 0 0 0-1.3-3.7A8 8 0 0 1 18.9 8zM12 4c.8 1.2 1.5 2.5 1.9 4h-3.8c.4-1.5 1.1-2.8 1.9-4zM4.3 14a8 8 0 0 1 0-4h3.4a16 16 0 0 0 0 4zm.8 2h3a15 15 0 0 0 1.3 3.7A8 8 0 0 1 5.1 16zm3-8h-3a8 8 0 0 1 4.3-3.7A15 15 0 0 0 8.1 8zM12 20c-.8-1.2-1.5-2.5-1.9-4h3.8c-.4 1.5-1.1 2.8-1.9 4zm2.3-6H9.7a14 14 0 0 1 0-4h4.6a14 14 0 0 1 0 4zm.3 5.7a15 15 0 0 0 1.3-3.7h3a8 8 0 0 1-4.3 3.7zm1.7-5.7a16 16 0 0 0 0-4h3.4a8 8 0 0 1 0 4z"/></svg>www.keystonefp.com</li>
  </ul>

  <p class="address">180 Harbor Street, Suite 210, Riverton, MI 49010</p>

  <div class="holder">
    <p class="holder__name">Marcus Ellery</p>
    <p class="holder__role">CEO/FOUNDER</p>
  </div>
</section>

<section class="card card--back" aria-label="Business card back">
  <div class="services">
    <p class="services__intro">We aggregate everything related to facilities maintenance, repair-replacement of equipment and facility space materials from:</p>
    <ul class="services__list">
      <li>Asset gathering and tracking</li>
      <li>Vendor screening, contracting and management</li>
      <li>Service requirement development</li>
      <li>Work order processing and management</li>
      <li>Invoice reconciliation</li>
      <li>Vendor payment</li>
      <li>Reporting</li>
      <li>Capital equipment bids and project management</li>
    </ul>
  </div>
  <aside class="back-panel">
    <div class="back-brand">
      <div class="back-brand__square"></div>
      <p class="back-brand__name">Keystone<br>Facility<br>Partners</p>
      <p class="back-brand__tagline">Maintain · Repair · Replace</p>
    </div>
  </aside>
</section>

</body>
</html>
```